Label design for an exciting new Vodka brand

We need a label design for a dynamic new Vodka brand called 'Pale lantern Vodka'. It is a crisp and versatile liquid with a clean and smooth finish. It should appeal to 21-39 year olds, with a slight female skew. Colours, fonts and styles should be modern and relatively neutral - take inspiration from the brand pictures attached.

Target Market(s)

21-39 year olds, both male and female, but with a slight female skew

```html
<!DOCTYPE html>
<html lang="en">
<head>
<meta charset="utf-8">
<title>Pale lantern Vodka – Label</title>
<link rel="stylesheet" href="https://fonts.googleapis.com/css2?family=Oswald:wght@500;600&family=Montserrat:wght@700&display=swap">
<style>
  :root {
    --paper: #eef1f5;
    --silver-dark: #8a8f95;
    --silver-light: #d9dde1;
    --teal-deep: #0a4766;
    --teal-mid: #2a86ad;
    --teal-soft: #6fb0cc;
    --ink-light: #e7ebef;
  }
  html, body {
    margin: 0;
    padding: 0;
    width: 1200px;
    height: 1200px;
    overflow: hidden;
    background: var(--paper);
  }
  .label {
    position: relative;
    width: 1200px;
    height: 1200px;
    background: var(--paper);
  }
  .silver-band {
    position: absolute;
    left: 0;
    width: 1200px;
    height: 20px;
    background: linear-gradient(180deg, var(--silver-light) 0%, var(--silver-dark) 45%, var(--silver-light) 70%, var(--silver-dark) 100%);
  }
  .silver-band--top { top: 180px; }
  .silver-band--bottom { top: 1000px; }
  .ornament {
    position: absolute;
    left: 400px;
    width: 400px;
    height: 90px;
    background: radial-gradient(ellipse at center, var(--teal-soft) 0%, rgba(111,176,204,0.35) 55%, rgba(238,241,245,0) 75%);
  }
  .ornament--top { top: 330px; }
  .ornament--bottom { top: 790px; }
  .plaque {
    position: absolute;
    left: 220px;
    top: 440px;
    width: 760px;
    height: 330px;
  }
  .plaque svg { display: block; width: 100%; height: 100%; }
  .brand-name {
    position: absolute;
    inset: 0;
    display: flex;
    flex-direction: column;
    align-items: center;
    justify-content: center;
    color: var(--ink-light);
    text-transform: uppercase;
    line-height: 1;
  }
  .brand-name__first {
    font-family: "Oswald", sans-serif;
    font-weight: 600;
    font-size: 104px;
    letter-spacing: 2px;
  }
  .brand-name__second {
    font-family: "Oswald", sans-serif;
    font-weight: 500;
    font-size: 40px;
    letter-spacing: 2px;
    margin-top: 4px;
  }
  .brand-name__category {
    font-family: "Montserrat", sans-serif;
    font-weight: 700;
    font-size: 104px;
    letter-spacing: 6px;
    margin-top: 6px;
  }
</style>
</head>
<body>
<main class="label">
  <div class="silver-band silver-band--top"></div>

  <div class="ornament ornament--top" role="img" aria-label="Decorative scroll flourish above the name plaque"></div>

  <div class="plaque">
    <svg viewBox="0 0 760 330" aria-hidden="true">
      <defs>
        <linearGradient id="plaque-fill" x1="0" y1="0" x2="1" y2="1">
          <stop offset="0" stop-color="#0a4766"/>
          <stop offset="0.45" stop-color="#2a86ad"/>
          <stop offset="0.7" stop-color="#1d6f96"/>
          <stop offset="1" stop-color="#0a4766"/>
        </linearGradient>
      </defs>
      <path d="M80,20 H680 A40,40 0 0 0 720,60 V110 Q760,165 720,220 V270 A40,40 0 0 0 680,310 H80 A40,40 0 0 0 40,270 V220 Q0,165 40,110 V60 A40,40 0 0 0 80,20 Z"
            fill="url(#plaque-fill)"/>
      <path d="M86,32 H674 A46,46 0 0 0 708,66 V113 Q744,165 708,217 V264 A46,46 0 0 0 674,298 H86 A46,46 0 0 0 52,264 V217 Q16,165 52,113 V66 A46,46 0 0 0 86,32 Z"
            fill="none" stroke="#cfe3ec" stroke-opacity="0.6" stroke-width="2"/>
    </svg>
    <h1 class="brand-name" style="margin:0">
      <span class="brand-name__first">Pale</span>
      <span class="brand-name__second">Lantern</span>
      <span class="brand-name__category">Vodka</span>
    </h1>
  </div>

  <div class="ornament ornament--bottom" role="img" aria-label="Decorative scroll flourish below the name plaque"></div>

  <div class="silver-band silver-band--bottom"></div>
</main>
</body>
</html>
```